Speisekarten-Design für persisches Restaurant
Zielgruppe
persisches Restaurant, möchte eine Karte mit schlichtem Design
Aufgabenstellung
bislang hatten wir ein Din A4 Karte mit vier Seiten. Kann gerne übernommen werden

```html
<!DOCTYPE html>
<html lang="de">
<head>
<meta charset="utf-8">
<title>NAVAZ – Speisekarte</title>
<link rel="stylesheet" href="https://fonts.googleapis.com/css2?family=Barlow+Condensed:ital,wght@0,400;0,500;1,400&display=swap">
<style>
  :root {
    --paper: #ffffff;
    --backdrop: #ffffff;
    --ink: #2b2725;
    --band: #353130;
    --gold: #a98451;
    --frame: #cdb593;
    --rule: #c8b08c;
    --muted: #4a4644;
  }
  * { box-sizing: border-box; margin: 0; padding: 0; }
  html, body { width: 1200px; height: 850px; overflow: hidden; background: var(--backdrop); }
  body { position: relative; font-family: "Barlow Condensed", "Arial Narrow", sans-serif; color: var(--ink); }

  .page {
    position: absolute; top: 78px; width: 510px; height: 722px;
    background: var(--paper);
    border: 1px solid #e4e1dc;
  }
  .page--front { left: 78px; }
  .page--back { left: 645px; }

  .page-frame {
    position: absolute; inset: 12px;
    border: 2px solid var(--frame);
  }
  .pattern-band {
    position: absolute; left: 20px; right: 20px; height: 24px;
    background: linear-gradient(180deg, var(--band), #463f3b);
  }
  .pattern-band--top { top: 20px; }
  .pattern-band--bottom { bottom: 20px; }

  /* front header */
  .lunch-badge {
    position: absolute; left: 33px; top: 65px; width: 86px; height: 86px;
    border-radius: 50%; background: var(--gold); color: #fff;
    display: flex; flex-direction: column; align-items: center; justify-content: center;
    transform: rotate(-14deg); text-align: center; line-height: 1;
  }
  .lunch-badge__title { font-size: 20px; font-weight: 400; letter-spacing: 0.5px; }
  .lunch-badge__hours { font-size: 6.5px; margin-top: 3px; line-height: 1.2; }

  .brand {
    position: absolute; left: 196px; top: 80px; width: 114px;
    display: flex; align-items: center; justify-content: center; gap: 6px;
  }
  .brand__dot { width: 12px; height: 12px; border-radius: 50%; background: var(--ink); }
  .brand__name { font-size: 34px; font-weight: 500; color: var(--ink); letter-spacing: 1px; }

  .phone {
    position: absolute; left: 348px; top: 117px;
    display: flex; align-items: center; gap: 6px;
    color: var(--gold); font-size: 15px; font-weight: 500;
  }
  .phone svg { width: 14px; height: 14px; }
  .web {
    position: absolute; left: 0; right: 0; top: 198px; text-align: center;
    color: var(--gold); font-size: 11px; font-weight: 500; letter-spacing: 0.5px;
  }

  .section-title {
    position: absolute; left: 28px; right: 28px;
    display: flex; align-items: center; gap: 8px;
    font-size: 15px; font-weight: 400; letter-spacing: 0.3px; white-space: nowrap;
  }
  .section-title::before, .section-title::after {
    content: ""; flex: 1; height: 2px; background: var(--rule);
  }
  .section-note {
    position: absolute; left: 28px; right: 28px; text-align: center;
    font-size: 6.5px; color: var(--ink);
  }

  .column {
    position: absolute; width: 222px;
    display: flex; flex-direction: column; gap: 9px;
  }
  .column--left { left: 28px; }
  .column--right { left: 262px; }

  .item-head {
    display: flex; align-items: baseline; gap: 2px;
    color: var(--gold); font-size: 11px; font-weight: 500; text-transform: uppercase; line-height: 1.2;
  }
  .item-head .tag { font-size: 6px; margin-left: 2px; }
  .item-head .leader { flex: 1; border-bottom: 1.5px dotted var(--gold); transform: translateY(-3px); }
  .item-head .price { font-size: 11px; }
  .item-de { font-size: 6.5px; line-height: 1.45; color: var(--muted); margin-top: 2px; }
  .item-en { font-size: 6.5px; line-height: 1.45; font-style: italic; color: var(--muted); margin-top: 2px; }
</style>
</head>
<body>

<!-- FRONT PAGE -->
<section class="page page--front" aria-label="Speisekarte Vorderseite">
  <div class="page-frame"></div>
  <div class="pattern-band pattern-band--top" role="img" aria-label="Zickzack-Ornamentband"></div>

  <div class="lunch-badge">
    <span class="lunch-badge__title">MITTAGS-<br>TISCH!</span>
    <span class="lunch-badge__hours">Montag - Freitag<br>11:00 - 16:00 Uhr</span>
  </div>

  <div class="brand">
    <span class="brand__dot"></span>
    <span class="brand__name">NAVAZ</span>
  </div>

  <div class="phone">
    <svg viewBox="0 0 24 24" aria-hidden="true"><path fill="#a98451" d="M6.6 10.8a15.1 15.1 0 0 0 6.6 6.6l2.2-2.2a1 1 0 0 1 1-.25 11.4 11.4 0 0 0 3.6.57 1 1 0 0 1 1 1V20a1 1 0 0 1-1 1A17 17 0 0 1 3 4a1 1 0 0 1 1-1h3.5a1 1 0 0 1 1 1c0 1.25.2 2.45.57 3.6a1 1 0 0 1-.25 1z"/></svg>
    <span>+49 69 55501234</span>
  </div>
  <div class="web">WWW.NAVAZ-ESSEN.DE</div>

  <h2 class="section-title" style="top:234px">VORSPEISEN // STARTERS</h2>

  <div class="column column--left" style="top:258px">
    <div class="item">
      <div class="item-head"><span>Kashke-Bademjan</span><span class="tag">G</span><span class="leader"></span><span class="price">9,50</span></div>
      <p class="item-de">Gebratene und gehackte Auberginen mit einem Hauch Knoblauch, Pfefferminzöl, Röstzwiebeln und Joghurt-Sauce (Kashk)</p>
      <p class="item-en">Chopped and fried aubergines with a touch of garlic, peppermint, roasted onions and yoghurt sauce (kashk)</p>
    </div>
    <div class="item">
      <div class="item-head"><span>Zeytun Parvarde</span><span class="tag">H</span><span class="leader"></span><span class="price">4,50</span></div>
      <p class="item-de">Grüne Oliven eingelegt in einer Kräuter-Granatapfel-Sauce. Mit Walnüssen und einem Hauch Knoblauch</p>
      <p class="item-en">Green olives marinated in a herb-pomegranate-sauce with walnuts and a touch of garlic</p>
    </div>
    <div class="item">
      <div class="item-head"><span>Borani Bademjan</span><span class="tag">G</span><span class="leader"></span><span class="price">4,50</span></div>
      <p class="item-de">Auberginen-Joghurt mit Knoblauch</p>
      <p class="item-en">Aubergine-yoghurt with garlic</p>
    </div>
    <div class="item">
      <div class="item-head"><span>Schafskäse</span><span class="tag">G</span><span class="leader"></span><span class="price">3,50</span></div>
      <p class="item-en">Feta cheese</p>
    </div>
    <div class="item">
      <div class="item-head"><span>Kräuterteller</span><span class="tag">G</span><span class="leader"></span><span class="price">4,00</span></div>
      <p class="item-de">Basilikum, Minze, Estragon, Petersilie, Schafskäse, Radieschen und Zwiebel</p>
      <p class="item-en">Basil, peppermint, tarragon, parsley, feta cheese, radishes and onion</p>
    </div>
  </div>

  <div class="column column--right" style="top:258px">
    <div class="item">
      <div class="item-head"><span>Mirza Ghassemi</span><span class="tag">C</span><span class="leader"></span><span class="price">9,50</span></div>
      <p class="item-de">Gegrillte und gehackte Auberginen mit einem Hauch Knoblauch, Tomaten und Ei</p>
      <p class="item-en">Chopped and grilled aubergines with a touch of garlic, tomatoes and egg</p>
    </div>
    <div class="item">
      <div class="item-head"><span>Borani</span><span class="tag">G</span><span class="leader"></span><span class="price">4,00</span></div>
      <p class="item-de">Spinat-Joghurt mit einem Hauch Knoblauch</p>
      <p class="item-en">Spinach-yoghurt with a touch of garlic</p>
    </div>
    <div class="item">
      <div class="item-head"><span>Dolmeh</span><span class="tag">G</span><span class="leader"></span><span class="price">4,00</span></div>
      <p class="item-de">Gefüllte Weinblätter (vegetarisch)</p>
      <p class="item-en">Stuffed vine leaves (vegetarian)</p>
    </div>
    <div class="item">
      <div class="item-head"><span>Hummus</span><span class="tag">K</span><span class="leader"></span><span class="price">5,00</span></div>
      <p class="item-de">Pürierte Kichererbsen mit einem Hauch Knoblauch und Sesam-Mus</p>
      <p class="item-en">Pureed chickpeas, sesame nutmeg and a touch of garlic</p>
    </div>
    <div class="item">
      <div class="item-head"><span>Gemischter Vorspeisenteller</span><span class="tag">(ab 2 Personen) G C H</span><span class="leader"></span><span class="price">p.P. 7,00</span></div>
      <p class="item-de">Pürierte Kichererbsen mit einem Hauch Knoblauch und Sesam-Mus</p>
      <p class="item-en">Pureed chickpeas, sesame nutmeg and a touch of garlic</p>
    </div>
    <div class="item">
      <div class="item-head"><span>Suppe Djo</span><span class="leader"></span><span class="price">5,00</span></div>
      <p class="item-de">Perlgraupensuppe</p>
      <p class="item-en">Barley soup</p>
    </div>
  </div>

  <h2 class="section-title" style="top:538px">SALATE // SALADS</h2>

  <div class="column column--left" style="top:563px">
    <div class="item">
      <div class="item-head"><span>Gemischter Salat</span><span class="tag">G</span><span class="leader"></span><span class="price">6,90</span></div>
      <p class="item-de">Salat, Gurken, Tomaten, Oliven, Schafskäse und Mais</p>
      <p class="item-en">Salad with lettuce, cucumbers, tomatoes, olives, feta cheese and maize</p>
    </div>
    <div class="item">
      <div class="item-head"><span>Salat Shirazi</span><span class="leader"></span><span class="price">3,00</span></div>
      <p class="item-de">Fein zerkleinerte Gurken, Tomaten und Zwiebeln, dazu Zitronensaft-Olivenöl-Dressing</p>
      <p class="item-en">Salad with finely chopped cucumbers, tomatoes, onions with lemon juice and olive oil dressing</p>
    </div>
  </div>

  <div class="column column--right" style="top:563px">
    <div class="item">
      <div class="item-head"><span>Grüner Salat</span><span class="tag">G</span><span class="leader"></span><span class="price">3,90</span></div>
      <p class="item-de">Salat, Gurken und Tomaten</p>
      <p class="item-en">Salad with lettuce, cucumbers and tomatoes</p>
    </div>
    <div class="item">
      <div class="item-head"><span>Salat Olvieh</span><span class="tag">C</span><span class="leader"></span><span class="price">6,00</span></div>
      <p class="item-de">Pürierter Kartoffelsalat mit Hähnchenbrust, Eiern und Salzgurken</p>
      <p class="item-en">Mashed potato salad with chicken breast, eggs and pickled cucumbers</p>
    </div>
  </div>

  <div class="pattern-band pattern-band--bottom" role="img" aria-label="Zickzack-Ornamentband"></div>
</section>

<!-- BACK PAGE -->
<section class="page page--back" aria-label="Speisekarte Rückseite">
  <div class="page-frame"></div>
  <div class="pattern-band pattern-band--top" role="img" aria-label="Zickzack-Ornamentband"></div>

  <h2 class="section-title" style="top:57px">REISGERICHTE // RICE DISHES</h2>

  <div class="column column--left" style="top:84px">
    <div class="item">
      <div class="item-head"><span>Baghali Polo ba Mahiche</span><span class="leader"></span><span class="price">16,00</span></div>
      <p class="item-de">Geschmorte Lammhaxe, serviert mit Basmatireis mit dicken Bohnen und Dillspitze, verfeinert mit Safran und Zimt</p>
      <p class="item-en">Braised knuckle of lamb; served with basmati rice with beans, dill tips and cinnamon</p>
    </div>
    <div class="item">
      <div class="item-head"><span>Sereshk Polo ba Mahiche</span><span class="leader"></span><span class="price">16,00</span></div>
      <p class="item-de">Geschmorte Lammhaxe, serviert mit Basmatireis mit gebratenen Berberitzen</p>
      <p class="item-en">Braised knuckle of lamb; served with basmati rice and fried berberis</p>
    </div>
    <div class="item">
      <div class="item-head"><span>Sereshk Polo ba Morgh</span><span class="leader"></span><span class="price">14,00</span></div>
      <p class="item-de">Geschmorte Hähnchenkeule, serviert mit Basmatireis und gebratenen Berberitzen</p>
      <p class="item-en">Braised chicken drumstick, served with basmati rice and fried berberis</p>
    </div>
  </div>

  <div class="column column--right" style="top:84px">
    <div class="item">
      <div class="item-head"><span>Baghali Polo ba Morgh</span><span class="leader"></span><span class="price">14,00</span></div>
      <p class="item-de">Geschmorte Hähnchenkeule, serviert mit Basmatireis mit dicken Bohnen und Dillspitze, verfeinert mit Safran und Zimt</p>
      <p class="item-en">Braised chicken drumstick, served with basmati rice with beans, dill tips and cinnamon</p>
    </div>
    <div class="item">
      <div class="item-head"><span>Shirin Polo ba Morgh</span><span class="leader"></span><span class="price">15,00</span></div>
      <p class="item-de">Geschmorte Hähnchenkeule, serviert mit Basmatireis und Mandelsplittern, gehackten Pistazien, Orangenschale und Karotten</p>
      <p class="item-en">Braised chicken drumstick, served with basmati rice with slivered almonds, chopped pistachios, orange peel and carrots</p>
    </div>
  </div>

  <h2 class="section-title" style="top:237px">VEGETARISCH &amp; VEGAN // VEGETARIAN &amp; VEGAN</h2>
  <p class="section-note" style="top:259px">Alle vegetarischen Gerichte werden mit Safran verfeinertem Basmatireis serviert // <i>All vegetarian dishes are served with saffron rice</i></p>

  <div class="column column--left" style="top:276px">
    <div class="item">
      <div class="item-head"><span>Bademjan vegetarisch</span><span class="tag">I</span><span class="leader"></span><span class="price">10,00</span></div>
      <p class="item-de">Auberginen in Tomatensauce</p>
      <p class="item-en">Aubergines in tomato sauce</p>
    </div>
    <div class="item">
      <div class="item-head"><span>Fesenjan</span><span class="tag">H</span><span class="leader"></span><span class="price">10,00</span></div>
      <p class="item-de">Gericht aus geriebenen Walnüssen und Granatapfelmark</p>
      <p class="item-en">Sauce made from grated walnut and pomegranate sauce</p>
    </div>
  </div>

  <div class="column column--right" style="top:276px">
    <div class="item">
      <div class="item-head"><span>Ghorme Sabsi vegetarisch</span><span class="leader"></span><span class="price">9,00</span></div>
      <p class="item-de">Gericht aus Bohnen, Limette und verschiedenen Kräutern (Schnittlauch, Petersilie, Bockshornklee)</p>
      <p class="item-en">Sauce made from beans, lemon and various herbs (chives, parsley, fenugreek)</p>
    </div>
    <div class="item">
      <div class="item-head"><span>Bamieh vegetarisch</span><span class="tag">I</span><span class="leader"></span><span class="price">10,00</span></div>
      <p class="item-de">Okraschoten in Tomatensauce</p>
      <p class="item-en">Okras in tomato sauce</p>
    </div>
  </div>

  <h2 class="section-title" style="top:395px">DESSERTS // DESSERTS</h2>

  <div class="column column--left" style="top:422px">
    <div class="item">
      <div class="item-head"><span>Bastani</span><span class="tag">G</span><span class="leader"></span><span class="price">4,50</span></div>
      <p class="item-de">Safraneis mit Pistazien und Sahnestückchen</p>
      <p class="item-en">Saffron ice cream with pistachios and cream pieces</p>
    </div>
    <div class="item">
      <div class="item-head"><span>Makhlut</span><span class="tag">G</span><span class="leader"></span><span class="price">5,00</span></div>
      <p class="item-de">Gemischtes Eis aus Bastani und Faludeh</p>
      <p class="item-en">Mix from Bastani and Faludeh</p>
    </div>
  </div>

  <div class="column column--right" style="top:422px">
    <div class="item">
      <div class="item-head"><span>Faludeh</span><span class="leader"></span><span class="price">4,50</span></div>
      <p class="item-de">Persisches Glasnudel-Sorbet</p>
      <p class="item-en">Persian glass noodle sorbet</p>
    </div>
    <div class="item">
      <div class="item-head"><span>Khorma ba Gerdu</span><span class="tag">H</span><span class="leader"></span><span class="price">5,00</span></div>
      <p class="item-de">Datteln mit Walnüssen gefüllt</p>
      <p class="item-en">Dates with walnut</p>
    </div>
    <div class="item">
      <div class="item-head"><span>Sholezard</span><span class="tag">H</span><span class="leader"></span><span class="price">4,00</span></div>
      <p class="item-de">Safran-Reispudding mit Zimt, Pistazien und Mandeln</p>
      <p class="item-en">Saffron rice pudding with cinnamon, pistachios and almonds</p>
    </div>
  </div>

  <div class="pattern-band pattern-band--bottom" role="img" aria-label="Zickzack-Ornamentband"></div>
</section>

</body>
</html>
```